Corwin Tably Interiors
business card and stationary
Corwin Tably Interiors -
Creative Brief
Simple
corwin tably
interior designer
studio: 27 brookfen lane pacifica, california 94044
corwin@corwintablyinteriors.example
http://corwintablyinteriors.example
the graphic part of my logo is something i will use a lot in my branding. i like the idea of repitition or a very large version of it in a single color or grayscale that bleeds off the card.
i like the grayscale logo (white burst) on the gray background a lot. i want one side of the card to be white background, probably the front.

```html
<!DOCTYPE html>
<html lang="en">
<head>
<meta charset="utf-8">
<title>Corwin Tably Interiors – Business Card</title>
<link rel="stylesheet" href="https://fonts.googleapis.com/css2?family=Questrial&family=Raleway:wght@300&display=swap">
<style>
  :root {
    --stage: #2b2b2c;
    --card-grey: #8d8d8f;
    --card-white: #ffffff;
    --ink-white: #ffffff;
    --ink-grey: #7a7a7a;
    --ink-dark: #3d3d3d;
    --sage: #b9d7a4;
    --sage-soft: #dcebd1;
    --mist: #a3a3a5;
  }
  * { margin: 0; padding: 0; box-sizing: border-box; }
  html, body {
    width: 1200px; height: 751px; overflow: hidden;
    background: var(--stage);
  }
  .stage { position: relative; width: 1200px; height: 751px; }

  .card {
    position: absolute; top: 211px;
    width: 576px; height: 336px; overflow: hidden;
  }
  .card--back  { left: 17px;  background: var(--card-grey); }
  .card--front { left: 619px; background: var(--card-white); }

  .brand-field { position: absolute; }
  .card--back .brand-field {
    left: 236px; top: 16px; width: 280px; height: 280px; border-radius: 50%;
    background: radial-gradient(circle, var(--mist) 0%, rgba(163,163,165,0.35) 55%, rgba(141,141,143,0) 72%);
  }
  .card--front .brand-field {
    left: -60px; top: -20px; width: 400px; height: 376px; border-radius: 50%;
    background: radial-gradient(circle, var(--sage-soft) 0%, var(--sage) 40%, rgba(185,215,164,0.25) 62%, rgba(255,255,255,0) 72%);
  }

  .brand {
    position: absolute; left: 14px; top: 158px;
    display: flex; align-items: center; gap: 12px;
  }
  .brand__dot {
    width: 46px; height: 46px; border-radius: 50%;
    background: var(--ink-white);
  }
  .brand__name {
    font-family: "Raleway", sans-serif; font-weight: 300;
    font-size: 34px; color: var(--ink-white); letter-spacing: -0.5px;
    line-height: 1;
  }

  .contact {
    position: absolute; right: 34px; top: 228px;
    text-align: right; font-style: normal;
    font-family: "Questrial", sans-serif; font-size: 15px;
    color: var(--ink-white); line-height: 19px;
  }
  .contact__address { margin-bottom: 6px; }

  .identity {
    position: absolute; right: 53px; top: 160px; text-align: right;
    font-family: "Questrial", sans-serif;
  }
  .identity__name { font-size: 21px; color: var(--sage); line-height: 22px; }
  .identity__role { font-size: 14px; color: var(--ink-grey); line-height: 16px; }

  .website {
    position: absolute; right: 27px; bottom: 28px;
    font-family: "Questrial", sans-serif; font-size: 17px;
    color: var(--ink-dark);
  }
</style>
</head>
<body>
  <main class="stage">
    <section class="card card--back" aria-label="Card back">
      <div class="brand-field" role="img" aria-label="Large faint brand symbol bleeding off the card"></div>
      <div class="brand">
        <span class="brand__dot"></span>
        <span class="brand__name">Corwin Tably Interiors</span>
      </div>
      <address class="contact">
        <p class="contact__address">studio: 27 brookfen lane<br>larkmere, westshire 00427</p>
        <p>415.555.0142</p>
        <p>corwin@corwintablyinteriors.example</p>
      </address>
    </section>

    <section class="card card--front" aria-label="Card front">
      <div class="brand-field" role="img" aria-label="Large sage-green brand symbol bleeding off the left edge"></div>
      <div class="identity">
        <p class="identity__name">corwintably</p>
        <p class="identity__role">interior designer</p>
      </div>
      <p class="website">www.corwintablyinteriors.example</p>
    </section>
  </main>
</body>
</html>
```